Home Page Design

Please see design brief attached. Concept here: mockboard[dot]net/file/qr83TpLM5wnePxHbUoKVsY/Velvetcourse---Landing-Page?node-id=0%3A1&t=KPwq7ZnRb2xTcVuM-1

Industry/Entity Type

Wedding

Number of Pages Required

1 page

Font styles to use
Serif
Sans Serif
Decorative
Script

Colors
A7469A
B969AE
D3A5CF
EDDBEB
F8F0F9
6B429C
8869AF
B7A5CE
E3DAEB
F3F0F8

Requirements
Must have
• Please see attached PDF
Nice to have
• Please see attached PDF
Should not have
• Please see attached PDF

```html
<!DOCTYPE html>
<html lang="en">
<head>
<meta charset="utf-8">
<title>Velvetcourse – Home</title>
<link rel="stylesheet" href="https://fonts.googleapis.com/css2?family=Nunito+Sans:wght@400;600;700&family=Great+Vibes&display=swap">
<style>
:root{
  --plum:#A7469A;--orchid:#B969AE;--mauve:#D3A5CF;--blush:#EDDBEB;--mist:#F8F0F9;
  --violet:#6B429C;--lavender:#8869AF;--lilac:#B7A5CE;--haze:#E3DAEB;--frost:#F3F0F8;
  --ink:#1c1c1c;--muted:#777;--footer:#5E4189;
}
*{box-sizing:border-box;margin:0;padding:0}
html,body{width:1200px;height:4692px;overflow:hidden}
body{position:relative;background:#fff;font-family:"Nunito Sans",Arial,sans-serif;color:var(--ink)}
.abs{position:absolute}
.btn{position:absolute;display:flex;align-items:center;justify-content:center;background:var(--lavender);color:#fff;font-size:12px;font-weight:600;border-radius:2px}
.photo{position:absolute}

/* header */
.header{position:absolute;top:0;left:0;width:1200px;height:140px;border-bottom:1px solid #eee}
.brand{position:absolute;display:flex;align-items:center;gap:10px;color:var(--violet);font-weight:700}
.brand .dot{width:22px;height:22px;border-radius:50%;background:var(--plum)}
.search{left:373px;top:22px;width:470px;height:38px;border:1px solid #ddd;border-radius:2px;display:flex;align-items:center;padding-left:12px;gap:8px;font-size:11px;color:#aaa}
.login{left:890px;top:25px;width:90px;height:33px}
.signup{left:990px;top:25px;width:90px;height:33px;background:#fff;color:var(--lavender);border:1px solid var(--lavender)}
.nav{position:absolute;top:82px;left:0;width:1200px;height:58px;border-top:1px solid #eee;font-size:14px}
.nav a{position:absolute;top:19px;color:var(--ink);text-decoration:none}
.nav a.active{border-bottom:3px solid var(--plum);padding-bottom:14px}

/* hero */
.hero{position:absolute;top:140px;left:0;width:1200px;height:500px;overflow:hidden}
.hero-title{position:absolute;top:160px;left:0;width:1250px;text-align:center;font-family:"Great Vibes",cursive;font-size:64px;line-height:64px;color:#fff}

/* stats */
.stat{position:absolute;display:flex;align-items:center;gap:14px}
.stat .ic{width:56px;height:56px;border-radius:50%;background:var(--blush);display:flex;align-items:center;justify-content:center}
.stat .ic i{width:24px;height:24px;border-radius:4px;background:var(--plum);opacity:.75}
.stat b{display:block;font-size:25px;color:var(--lavender);font-weight:700;line-height:26px}
.stat span{font-size:15px}
.stat-card{position:absolute;left:546px;top:688px;width:252px;height:95px;background:#fff;box-shadow:0 8px 24px rgba(0,0,0,.12)}

/* intro */
.intro-title{left:122px;top:912px;font-size:28px;line-height:31px;font-weight:600}
.intro-text{left:118px;top:994px;font-size:12.5px;line-height:15px;width:340px}

/* testimonials */
.reviews{position:absolute;top:1202px;left:0;width:1200px;height:464px;background:linear-gradient(#fff 20%,var(--blush))}
.sec-title{position:absolute;left:0;width:1200px;text-align:center;font-size:27px;font-weight:600}
.arrow{position:absolute;width:32px;height:32px;background:#fff;border:1px solid #ddd;display:flex;align-items:center;justify-content:center}
.review{position:absolute;top:124px;width:279px;height:196px;background:#fff;box-shadow:0 4px 16px rgba(0,0,0,.1)}
.review:after{content:"";position:absolute;left:34px;bottom:-14px;border:8px solid transparent;border-top:8px solid #fff}
.vendor{position:absolute;left:14px;top:16px;width:250px;height:86px;background:#f7f7f7;border:1px solid #e4e4e4;display:flex;align-items:center;gap:14px;padding-left:20px}
.vendor .thumb{width:50px;height:48px}
.vendor b{font-size:12px;display:block;font-weight:700}
.stars{color:var(--lavender);font-size:13px;letter-spacing:1px}
.review p{position:absolute;left:18px;top:122px;width:245px;font-size:11px;line-height:15px;color:var(--muted)}
.reviewer{position:absolute;top:342px;display:flex;align-items:center;gap:14px}
.reviewer .av{width:44px;height:44px;border-radius:50%;background:linear-gradient(135deg,#c9b3a3,#4b3a36)}
.reviewer b{font-size:14px;font-weight:600;display:block}
.reviewer span{font-size:11px;color:#999}

/* how it works */
.how{position:absolute;top:1666px;left:0;width:1200px;height:690px;background:linear-gradient(var(--plum),var(--orchid) 25%,var(--blush) 75%,#fff)}
.step{position:absolute;top:155px;width:277px;height:255px;background:#fff;text-align:center;box-shadow:0 4px 14px rgba(0,0,0,.08)}
.step.alt{background:var(--haze);border:1px solid var(--lilac)}
.step .num{position:absolute;left:102px;top:-28px;width:72px;height:72px;border-radius:50%;background:var(--haze);border:4px solid #fff;font-size:24px;display:flex;align-items:center;justify-content:center}
.step h3{position:absolute;left:0;width:100%;top:72px;font-size:19px;line-height:20px;font-weight:400;color:var(--plum)}
.step p{position:absolute;left:32px;width:213px;top:132px;font-size:10px;line-height:14px;color:#333}
.dash{position:absolute;left:146px;top:443px;width:937px;border-top:1.5px dashed #999}
.insured h3{position:absolute;left:400px;top:498px;font-size:25px;line-height:27px;font-weight:600}
.insured p{position:absolute;left:400px;top:558px;width:520px;font-size:10px;line-height:13px;color:#333}

/* marketplace */
.tile{position:absolute;width:208px;height:69px;background:#fff;box-shadow:0 3px 10px rgba(0,0,0,.1);display:flex;align-items:center}
.tile .pic{width:87px;height:69px;flex:none}
.tile span{flex:1;text-align:center;font-size:13px;line-height:15px}

/* pdf banner */
.pdf{position:absolute;top:3061px;left:0;width:1200px;height:381px;background:linear-gradient(90deg,#f5f1f6 40%,#e6dbe5 65%,#cdbdcb);overflow:hidden}
.pdf h2{position:absolute;left:162px;top:138px;font-size:26px;line-height:28px;font-weight:500}

/* promo */
.promo{position:absolute;top:3496px;width:426px;height:256px;border:1px solid #ddd;overflow:hidden;text-align:center}
.promo .bg{position:absolute;inset:0;background:linear-gradient(#fff 45%,#e9e4e8 70%,#b9ada7)}
.promo h3{position:absolute;left:0;width:100%;top:32px;font-size:25px;font-weight:500;color:var(--plum)}
.promo p{position:absolute;left:60px;width:306px;top:82px;font-size:12px;line-height:15px}
.promo .btn{left:140px;top:158px;width:146px;height:38px;background:var(--plum);font-size:12px}
.dots{position:absolute;top:3806px;left:574px;display:flex;gap:10px}
.dots i{width:9px;height:9px;border-radius:50%;background:#ddd}
.dots i.on{background:var(--lavender)}

/* link directory */
.directory{position:absolute;top:3866px;left:0;width:1200px;border-top:1px solid #e6e6e6}
.col{position:absolute;top:54px}
.col h4{font-size:18px;font-weight:700;color:var(--lavender);margin-bottom:14px}
.col li{list-style:none;font-size:12px;line-height:18.4px;color:var(--lavender)}

/* footer */
.footer{position:absolute;top:4434px;left:0;width:1200px;height:258px;background:var(--footer);color:#fff}
.fcol{position:absolute;top:40px}
.fcol h5{font-size:14px;font-weight:600;margin-bottom:10px}
.fcol li{list-style:none;font-size:12px;line-height:23px}
.subscribe{position:absolute;left:883px;top:73px;width:204px;height:31px;display:flex;font-size:11px}
.subscribe .field{flex:1;background:#fff;color:#222;display:flex;align-items:center;padding-left:10px}
.subscribe .send{width:56px;background:#eee;color:#222;font-weight:700;display:flex;align-items:center;justify-content:center}
.social{position:absolute;left:893px;top:129px;display:flex;gap:12px}
.social i{width:16px;height:16px;border-radius:50%;background:#fff}
.rule{position:absolute;left:98px;top:186px;width:1003px;border-top:1px solid rgba(255,255,255,.4)}
.copy{position:absolute;top:208px;width:1200px;text-align:center;font-size:11px}
</style>
</head>
<body>

<header class="header">
  <div class="brand" style="left:117px;top:26px;font-size:24px"><span class="dot"></span>Velvetcourse</div>
  <div class="abs search"><svg width="12" height="12" viewBox="0 0 12 12"><circle cx="5" cy="5" r="4" fill="none" stroke="#A7469A" stroke-width="1.5"/><line x1="8" y1="8" x2="11" y2="11" stroke="#A7469A" stroke-width="1.5"/></svg>Search</div>
  <div class="btn login">LOGIN</div>
  <div class="btn signup">SIGN UP</div>
  <nav class="nav">
    <a class="active" style="left:126px">Home</a>
    <a style="left:217px">Menu 2</a>
    <a style="left:319px">Menu 3</a>
    <a style="left:424px">Menu 4</a>
    <a style="left:524px">Menu 5</a>
  </nav>
</header>

<section class="hero">
  <div class="photo" role="img" aria-label="Close-up of a couple's hands exchanging a wedding ring beside a bouquet" style="inset:0;background:linear-gradient(120deg,#6d645f,#a49891 35%,#8c7f78 60%,#5a4f4c)"></div>
  <h1 class="hero-title">Be the couple who stuck to<br>their budget!</h1>
  <div class="btn" style="left:574px;top:341px;width:103px;height:38px;background:var(--plum)">Explore</div>
  <svg class="abs" style="left:0;top:0" width="1200" height="500" viewBox="0 0 1200 500">
    <path d="M0 418 C300 440 800 430 1200 410 L1200 500 L0 500Z" fill="#A7469A"/>
    <path d="M0 440 C350 480 800 450 1200 450 L1200 500 L0 500Z" fill="#fff"/>
  </svg>
</section>

<div class="stat" style="left:121px;top:712px"><div class="ic"><i></i></div><div><b>700</b><span>Venues</span></div></div>
<div class="stat" style="left:342px;top:712px"><div class="ic"><i></i></div><div><b>1500</b><span>Vendors</span></div></div>
<div class="stat-card"></div>
<div class="stat" style="left:572px;top:707px"><div class="ic"><i></i></div><div><b>500</b><span>Wedding Booked</span></div></div>
<div class="stat" style="left:864px;top:720px"><div class="ic"><i></i></div><div><b>$7.680</b><span>Average Saved</span></div></div>

<h2 class="abs intro-title">Because life is too short to<br>wait for vendors to reply</h2>
<p class="abs intro-text">Focus on enjoying your wedding! Don't get tied into endless negotiations and emails.</p>
<div class="btn" style="left:118px;top:1056px;width:106px;height:39px">Explore</div>
<div class="photo" role="img" aria-label="Outdoor ceremony aisle with white chairs and a floral arch under pine trees" style="left:606px;top:852px;width:594px;height:328px;background:linear-gradient(#8fb0d4,#c7d6e6 40%,#d9d4d0 70%,#8a7461)"></div>

<section class="reviews">
  <h2 class="sec-title" style="top:64px">Our Customer Loves Us</h2>
  <div class="arrow" style="left:117px;top:219px"><svg width="12" height="12" viewBox="0 0 12 12"><path d="M11 6H1M5 2L1 6l4 4" fill="none" stroke="#8869AF" stroke-width="1.4"/></svg></div>
  <div class="arrow" style="left:1046px;top:230px"><svg width="12" height="12" viewBox="0 0 12 12"><path d="M1 6h10M7 2l4 4-4 4" fill="none" stroke="#8869AF" stroke-width="1.4"/></svg></div>

  <div class="review" style="left:169px">
    <div class="vendor"><div class="thumb" role="img" aria-label="Vendor venue photo" style="background:linear-gradient(#6b8aa0,#8a5e3c)"></div><div><b>Name Vendor</b><span class="stars">★★★★★</span></div></div>
    <p>Lorem ipsum dolor sit amet consectetur. Donec egestas sagittis purus in etiam volutpat felis. At praesent malesuada</p>
  </div>
  <div class="review" style="left:463px">
    <div class="vendor"><div class="thumb" role="img" aria-label="Vendor bouquet photo" style="background:linear-gradient(#3e3330,#c9b6a4)"></div><div><b>Name Vendor</b><span class="stars">★★★★★</span></div></div>
    <p>Lorem ipsum dolor sit amet consectetur. Donec egestas sagittis purus in etiam volutpat felis. At praesent malesuada</p>
  </div>
  <div class="review" style="left:756px">
    <div class="vendor"><div class="thumb" role="img" aria-label="Vendor table setting photo" style="background:linear-gradient(#e4e9e0,#9fb28a)"></div><div><b>Name Vendor</b><span class="stars">★★★★★</span></div></div>
    <p>Lorem ipsum dolor sit amet consectetur. Donec egestas sagittis purus in etiam volutpat felis. At praesent malesuada</p>
  </div>

  <div class="reviewer" style="left:191px"><div class="av" role="img" aria-label="Customer portrait"></div><div><b>Clara Wynn</b><span>November, 2022</span></div></div>
  <div class="reviewer" style="left:484px"><div class="av" role="img" aria-label="Customer portrait"></div><div><b>Dana Holtby</b><span>November, 2022</span></div></div>
  <div class="reviewer" style="left:778px;top:338px"><div class="av" role="img" aria-label="Customer portrait"></div><div><b>Rina Solvera Anwar</b><span>October, 2022</span></div></div>
</section>

<section class="how">
  <h2 class="sec-title" style="top:84px;color:#fff;font-weight:500">How it Works</h2>
  <div class="step" style="left:166px"><div class="num">1</div><h3 style="top:82px">Browse Top Vendors</h3><p>Lorem ipsum dolor sit amet, consectetur adipiscing elit. Suspendisse ac bibendum nibh. Nulla tempor nibh ex, ac sodales augue tempus sit amet. Morbi at turpis auctor, venenatis ipsum et.</p></div>
  <div class="step alt" style="left:475px"><div class="num">2</div><h3>Instantly Book with<br>Pre-negotiated Prices</h3><p style="top:126px">Lorem ipsum dolor sit amet, consectetur adipiscing elit. Suspendisse ac bibendum nibh. Nulla tempor nibh ex, ac sodales augue tempus sit amet. Morbi at turpis auctor, venenatis ipsum et.</p></div>
  <div class="step" style="left:785px"><div class="num" style="top:-34px">3</div><h3 style="top:64px">Pay Over Time</h3><p style="top:122px">Lorem ipsum dolor sit amet, consectetur adipiscing elit. Suspendisse ac bibendum nibh. Nulla tempor nibh ex, ac sodales augue tempus sit amet. Morbi at turpis auctor, venenatis ipsum et.</p></div>
  <div class="dash"></div>
  <svg class="abs" style="left:303px;top:500px" width="68" height="82" viewBox="0 0 68 82"><path d="M34 3 L64 14 V40 C64 60 50 72 34 79 C18 72 4 60 4 40 V14Z" fill="none" stroke="#A7469A" stroke-width="5"/><path d="M34 14 L54 22 V40 C54 55 45 63 34 68 C23 63 14 55 14 40 V22Z" fill="#A7469A"/><path d="M24 41 l8 8 l14 -16" fill="none" stroke="#fff" stroke-width="4"/></svg>
  <div class="insured"><h3>Velvetsafe! - Because life happens. All your<br>bookings are fully insured</h3><p>Lorem ipsum dolor sit amet, consectetur adipiscing elit. Suspendisse ac bibendum nibh. Nulla tempor nibh ex, ac sodales augue tempus sit amet. Morbi at turpis auctor, venenatis ipsum et.</p></div>
</section>

<h2 class="sec-title" style="top:2398px;font-size:26px">Explore our Marketplace</h2>
<p class="abs" style="top:2442px;left:0;width:1200px;text-align:center;font-size:12.5px">Focus on enjoying your wedding! Don't get tied into endless negotiations and emails.</p>

<div class="tile" style="left:166px;top:2497px"><div class="pic" role="img" aria-label="Garden venue" style="background:linear-gradient(#9bb7c9,#6f8f55)"></div><span>Venues</span></div>
<div class="tile" style="left:397px;top:2497px"><div class="pic" role="img" aria-label="Photographer at work" style="background:linear-gradient(#d6d0c8,#5b4b42)"></div><span>Photographers</span></div>
<div class="tile" style="left:625px;top:2497px"><div class="pic" role="img" aria-label="DJ booth lights" style="background:linear-gradient(#2a1845,#c0399a)"></div><span>DJs</span></div>
<div class="tile" style="left:854px;top:2497px"><div class="pic" role="img" aria-label="Bridal makeup" style="background:linear-gradient(#e9ddd6,#b48b72)"></div><span>Hair &amp; Make up</span></div>

<div class="tile" style="left:166px;top:2575px"><div class="pic" role="img" aria-label="Planner with notes" style="background:linear-gradient(#c89a6a,#6c4a2e)"></div><span>Planners</span></div>
<div class="tile" style="left:397px;top:2575px"><div class="pic" role="img" aria-label="Catering buffet" style="background:linear-gradient(#b88456,#5e3b22)"></div><span>Caterers</span></div>
<div class="tile" style="left:625px;top:2575px"><div class="pic" role="img" aria-label="Flower arrangements" style="background:linear-gradient(#cf6a5e,#6f7a4a)"></div><span>Florist</span></div>
<div class="tile" style="left:854px;top:2575px"><div class="pic" role="img" aria-label="Video camera" style="background:linear-gradient(#d8a04a,#2d2a28)"></div><span>Videographers</span></div>

<div class="tile" style="left:166px;top:2653px"><div class="pic" role="img" aria-label="Ceremony officiant" style="background:linear-gradient(#8a8a55,#3f3a28)"></div><span>Officiants</span></div>
<div class="tile" style="left:397px;top:2653px"><div class="pic" role="img" aria-label="Rental tent and tables" style="background:linear-gradient(#f1ede6,#a89f92)"></div><span>Rentals</span></div>
<div class="tile" style="left:625px;top:2653px"><div class="pic" role="img" aria-label="Photo booth" style="background:linear-gradient(#cfcfcf,#1f1f1f)"></div><span>Photo Booths</span></div>
<div class="tile" style="left:854px;top:2653px"><div class="pic" role="img" aria-label="Live band on stage" style="background:linear-gradient(#d94a6b,#3a1a3a)"></div><span>Bands</span></div>

<div class="tile" style="left:166px;top:2732px"><div class="pic" role="img" aria-label="Wedding dresses" style="background:linear-gradient(#ece6e2,#c0a99a)"></div><span>Dresses &amp;<br>Attire</span></div>
<div class="tile" style="left:397px;top:2732px"><div class="pic" role="img" aria-label="Wedding cake" style="background:linear-gradient(#f4f2ee,#cfc6bc)"></div><span>Cakes</span></div>
<div class="tile" style="left:625px;top:2732px"><div class="pic" role="img" aria-label="White limousine" style="background:linear-gradient(#e8ecef,#9aa2a8)"></div><span>Limos/<br>Transportation</span></div>
<div class="tile" style="left:854px;top:2732px"><div class="pic" role="img" aria-label="Musician performing" style="background:linear-gradient(#2d3c7a,#0f0f1f)"></div><span>Musician/<br>Ceremony</span></div>

<div class="tile" style="left:166px;top:2812px"><div class="pic" role="img" aria-label="Decor and lighting" style="background:linear-gradient(#9c8467,#4a3b2c)"></div><span>Decor &amp;<br>Lighting</span></div>
<div class="tile" style="left:397px;top:2812px"><div class="pic" role="img" aria-label="Printed invitations" style="background:linear-gradient(#eef0f2,#9aa3ad)"></div><span>Invitations</span></div>
<div class="tile" style="left:625px;top:2812px"><div class="pic" role="img" aria-label="Airplane at sunset" style="background:linear-gradient(#2c4d7a,#e89a4a)"></div><span>Travel Agents</span></div>
<div class="tile" style="left:854px;top:2812px"><div class="pic" role="img" aria-label="Wedding rings" style="background:linear-gradient(#b7b9a3,#5e6a52)"></div><span>Jewelers</span></div>

<div class="tile" style="left:166px;top:2890px"><div class="pic" role="img" aria-label="Wedding favors" style="background:linear-gradient(#e6d3b5,#b08a5a)"></div><span>Favors &amp;<br>Gifts</span></div>
<div class="tile" style="left:397px;top:2890px"><div class="pic" role="img" aria-label="Day-of coordinator" style="background:linear-gradient(#8fb36a,#c4403c)"></div><span>Day of Wedding<br>Coordinators</span></div>
<div class="tile" style="left:625px;top:2890px"><div class="pic" role="img" aria-label="Couple dancing" style="background:linear-gradient(#9aa88a,#45503a)"></div><span>Dance Lessons</span></div>

<section class="pdf">
  <div class="photo" role="img" aria-label="Bride and groom embracing under a veil" style="left:590px;top:0;width:610px;height:381px;background:linear-gradient(90deg,rgba(245,241,246,0),#d8c9c4 35%,#8a8593 60%,#c9bfcc)"></div>
  <h2>Download our free PDF and<br>start down the road to saving money</h2>
  <div class="btn" style="left:162px;top:213px;width:128px;height:37px">Download PDF</div>
</section>

<div class="arrow" style="left:93px;top:3602px"><svg width="12" height="12" viewBox="0 0 12 12"><path d="M11 6H1M5 2L1 6l4 4" fill="none" stroke="#A7469A" stroke-width="1.4"/></svg></div>
<div class="arrow" style="left:1073px;top:3618px"><svg width="12" height="12" viewBox="0 0 12 12"><path d="M1 6h10M7 2l4 4-4 4" fill="none" stroke="#A7469A" stroke-width="1.4"/></svg></div>
<div class="promo" style="left:162px">
  <div class="bg" role="img" aria-label="White roses and table flowers"></div>
  <h3>Reclaims Your Sanity</h3>
  <p>Lorem ipsum dolor sit amet consectetur. Suscipit scelerisque vestibulum si</p>
  <div class="btn">BOOK TODAY!</div>
</div>
<div class="promo" style="left:610px">
  <div class="bg" role="img" aria-label="Bridal bouquet in soft light"></div>
  <h3 style="top:50px">Get 40% Disc</h3>
  <p style="top:98px">Lorem ipsum dolor sit amet consectetur. Suscipit scelerisque vestibulum si</p>
  <div class="btn" style="top:150px">BOOK TODAY!</div>
</div>
<div class="dots"><i></i><i></i><i class="on"></i></div>

<section class="directory">
  <div class="col" style="left:107px;top:44px"><h4>Local Services</h4><ul>
    <li>Wedding Photographers</li><li>Wedding DJs</li><li>Wedding Hair &amp; Makeup</li><li>Wedding Planners</li><li>Wedding Caterers</li><li>Wedding Florists</li><li>Wedding Videographers</li><li>Wedding Officiants</li><li>Wedding Rentals</li><li>Wedding Photo Booths</li><li>Wedding Bands</li><li>Wedding Dresses &amp; Attire</li><li>Wedding Cakes</li><li>Wedding Limos / Transportation</li><li>Wedding Musicians / Ceremony Music</li><li>Wedding Decor &amp; Lighting</li><li>Wedding Invitations</li><li>Travel Agents</li><li>Wedding Jewelers</li><li>Wedding Favors &amp; Gifts</li><li>Day Of Wedding Coordinators</li><li>Wedding Dance Lessons</li></ul></div>
  <div class="col" style="left:373px;top:46px"><h4>Digital Services</h4><ul>
    <li>Logo Design</li><li>Portaits &amp; Caricatures</li><li>Video Editing</li><li>Invitation Design</li><li>Image Editing</li><li>Slideshow Videos</li><li>Speechwriting</li><li>Greeting Cards &amp; Videos</li></ul></div>
  <div class="col" style="left:641px;top:46px"><h4>Support</h4><ul>
    <li>Help &amp; Support</li><li>Trust &amp; Safety</li><li>Selling on Velvetcourse</li><li>Buying on Velvetcourse</li></ul></div>
  <div class="col" style="left:881px;top:46px"><h4>More from Velvetcourse</h4><ul>
    <li>Velvetcourse Business</li><li>Velvetcourse Pro</li><li>Careers</li><li>Press &amp; News</li><li>Partnership</li><li>Privacy Policy</li><li>Terms of Service</li></ul></div>
</section>

<footer class="footer">
  <div class="brand" style="left:100px;top:70px;font-size:22px;color:#fff"><span class="dot" style="background:#fff"></span>Velvetcourse</div>
  <div class="fcol" style="left:357px"><h5>COMPANY</h5><ul><li>About Us</li><li>Careers</li><li>Contact Us</li><li>News</li></ul></div>
  <div class="fcol" style="left:477px"><h5>QUICK LINKS</h5><ul><li>Wedding Vendors</li><li>Wedding Hair &amp; Beauty</li><li>Wedding Caterers</li></ul></div>
  <div class="fcol" style="left:652px"><h5>INFORMATIONS</h5><ul><li>Contact Center</li><li>Privacy Policy</li><li>Terms of Use</li></ul></div>
  <div class="fcol" style="left:883px;top:43px"><h5>STAY UP TO DATE!</h5></div>
  <div class="subscribe"><div class="field">your email</div><div class="send">SEND</div></div>
  <div class="social"><i></i><i></i><i></i><i></i><i></i></div>
  <div class="rule"></div>
  <p class="copy">Copyright 2023 Velvetcourse. All rights reserved.</p>
</footer>

</body>
</html>
```